RollUp Druck 85x200cm für Finanzdienstleister
Zielgruppe
Die kwa Stock GmbH stellt unter ihrer Marke "Hausfond-Lotse" Baufinanzierungsberatern professionelle Lösungen zur Finanzierungsabwicklung zur Verfügung. Nähere Informationen rund um das Unternehmen erhalten Sie unter www.hausfond-lotse.de.
Aufgabenstellung
Als ergänzende Marketingmaßnahme ist die Anschaffung von RollUps geplant. Für diese wünschen wir uns ein thematisch zur Kundenkommunikation passendes RollUp mit den obigen Maßen und den Werbeslogan "Baufinanzierung - seriöse Beratung und beste Konditionen aus über 100 Banken". Die Grafik soll sich an den branchenüblichen Motiven orientieren, aber auch für frische Ideen sind wir offen.
Alle mit 5 Sterne bewerteten Entwürfe werden wir von den entsprechenden Designer zum angebotenen Preis kaufen (sprich 4 Entwürfe mit 5 Sternen = 5x Preisgeld).

```html
<!DOCTYPE html>
<html lang="de">
<head>
<meta charset="utf-8">
<title>Hausfond-Lotse RollUp</title>
<link rel="stylesheet" href="https://fonts.googleapis.com/css2?family=Source+Sans+3:wght@400;600&display=swap">
<style>
  :root {
    --stage: #d9dbd8;
    --paper: #ffffff;
    --paper-fade: #ecedef;
    --brand-blue: #1f6fc0;
    --band-dark: #1784e0;
    --band-light: #35b8f2;
    --ink: #2b2f36;
    --ink-soft: #4a4f57;
    --title-box: rgba(140, 142, 150, 0.42);
    --white: #ffffff;
  }
  * { margin: 0; padding: 0; box-sizing: border-box; }
  html, body {
    width: 1200px; height: 900px; overflow: hidden;
    background: var(--stage);
    font-family: "Source Sans 3", "Myriad Pro", sans-serif;
  }
  .rollup {
    position: absolute; left: 417px; top: 20px;
    width: 366px; height: 860px;
    background: linear-gradient(to bottom, var(--paper) 0%, var(--paper) 65%, var(--paper-fade) 100%);
    box-shadow: 0 6px 24px rgba(0,0,0,0.18);
    overflow: hidden;
  }
  .hero-photo {
    position: absolute; left: 80px; top: 40px; width: 286px; height: 300px;
    background: radial-gradient(ellipse at 55% 55%, #c9d3dd 0%, #e4e2e6 40%, #f6f6f7 70%, var(--paper) 100%);
  }
  .headline-box {
    position: absolute; left: 0; top: 62px; width: 250px; height: 132px;
    background: var(--title-box);
    color: var(--white);
    padding: 8px 10px;
  }
  .headline-box h1 { font-weight: 400; font-size: 29px; line-height: 1.05; letter-spacing: 0.2px; }
  .headline-box p { font-size: 16.5px; line-height: 1.2; margin-top: 4px; }
  .contact-band { position: absolute; left: 0; top: 0; width: 366px; height: 860px; }
  .band-text { fill: var(--white); font-family: "Source Sans 3", sans-serif; }
  .benefits {
    position: absolute; left: 32px; top: 465px; list-style: none;
  }
  .benefits li {
    display: flex; align-items: center; gap: 10px;
    font-size: 15.5px; color: var(--ink); height: 42px;
  }
  .benefits svg { width: 20px; height: 12px; flex: none; }
  .about { position: absolute; left: 32px; top: 650px; width: 300px; }
  .about h2 { font-weight: 400; font-size: 17px; color: var(--brand-blue); margin-bottom: 8px; }
  .about p { font-size: 9.6px; line-height: 1.35; color: var(--ink-soft); margin-bottom: 9px; }
  .brand { position: absolute; left: 32px; top: 770px; display: flex; align-items: center; gap: 8px; }
  .brand-square { width: 18px; height: 18px; background: var(--brand-blue); }
  .brand-name { font-size: 18px; font-weight: 600; color: var(--brand-blue); }
  .contact { position: absolute; left: 32px; top: 806px; font-size: 9.6px; line-height: 1.35; color: var(--ink); }
</style>
</head>
<body>
  <section class="rollup">
    <div class="hero-photo" role="img" aria-label="Foto eines kleinen Hauses, gefaltet aus Euro-Geldscheinen"></div>

    <div class="headline-box">
      <h1>Baufinanzierung</h1>
      <p>- seriöse Beratung und beste Konditionen aus über 100 Banken</p>
    </div>

    <svg class="contact-band" viewBox="0 0 366 860">
      <polygon points="0,275 190,363 250,461 0,345" fill="var(--band-dark)"/>
      <polygon points="190,363 366,445 366,575 250,461" fill="var(--band-light)"/>
      <text class="band-text" font-size="12.5" transform="translate(8,300) rotate(24.9)">Noch Fragen? 030 - 412 78 093</text>
      <text class="band-text" font-size="11.5" transform="translate(226,397) rotate(38)">www.hausfond-lotse.de</text>
    </svg>

    <ul class="benefits">
      <li><svg viewBox="0 0 20 12"><path d="M0 6H18M13 1L18.5 6L13 11" fill="none" stroke="var(--brand-blue)" stroke-width="1.3"/></svg>über 100 Banken im Vergleich</li>
      <li><svg viewBox="0 0 20 12"><path d="M0 6H18M13 1L18.5 6L13 11" fill="none" stroke="var(--brand-blue)" stroke-width="1.3"/></svg>kostenlose &amp; verbindliche Beratung</li>
      <li><svg viewBox="0 0 20 12"><path d="M0 6H18M13 1L18.5 6L13 11" fill="none" stroke="var(--brand-blue)" stroke-width="1.3"/></svg>persönliche Beratung vor Ort</li>
      <li><svg viewBox="0 0 20 12"><path d="M0 6H18M13 1L18.5 6L13 11" fill="none" stroke="var(--brand-blue)" stroke-width="1.3"/></svg>zertifizierte Berater</li>
    </ul>

    <div class="about">
      <h2>Beratung spart Geld</h2>
      <p>Die Hausfond-Lotse (eine Marke der kwa Stock GmbH) stehen Ihnen regional vor Ort persönlich zur Verfügung. Nutzen Sie dazu unsere komfortable Beratersuche.</p>
      <p>Für alle weiteren Fragen steht ihnen unser Innendienst gern zur Verfügung.</p>
    </div>

    <div class="brand">
      <span class="brand-square"></span>
      <span class="brand-name">Hausfond-Lotse</span>
    </div>

    <div class="contact">
      Hr. Wendlandt<br>
      Telefon 030 – 412 78 093 10<br>
      Email j.wendlandt@hausfond-lotse.de
    </div>
  </section>
</body>
</html>
```